We need a letterhead incorporating our logo (uploaded file), with the name of our organization (Ashbourne Vale Borough Police Association) and our slogan (Strength in Unity). Dark blue should be incorporated somewhere in the design, either the font color or elsewhere. Please make sure our logo is included in the design. The organization is a law enforcement union type group.

Target Market(s)

Members of our association, policticians, and anyone receiving our letters

Colors
0255a3

Requirements
Must have
• Our logo, Association name, and slogan.
Nice to have
• A professional and eye-catching letterhead design incorporating the logo, name, and slogan.

```html
<!DOCTYPE html>
<html lang="en">
<head>
<meta charset="utf-8">
<title>Ashbourne Vale Borough Police Association Letterhead</title>
<link href="https://fonts.googleapis.com/css2?family=Libre+Caslon+Text:wght@700&family=Poppins:wght@400;500;600&family=Open+Sans:wght@400&family=Great+Vibes&display=swap" rel="stylesheet">
<style>
  :root {
    --brand-blue: #0255a3;
    --accent-blue: #1d4fa8;
    --slogan-gold: #fcc078;
    --ink: #2f3136;
    --muted: #8a8f9c;
    --navy: #1c2a44;
    --backdrop: #a9a9a9;
    --paper: #ffffff;
  }
  * { margin: 0; padding: 0; box-sizing: border-box; }
  html, body { width: 1200px; height: 1200px; overflow: hidden; }
  body { background: var(--backdrop); position: relative; font-family: "Open Sans", sans-serif; }

  .letterhead {
    position: absolute; left: 135px; top: 0;
    width: 929px; height: 1200px;
    background: var(--paper);
  }

  .brand-mark {
    position: absolute; top: 22px; left: 0; width: 100%;
    display: flex; flex-direction: column; align-items: center; gap: 10px;
  }
  .brand-mark__circle {
    width: 86px; height: 86px; border-radius: 50%;
    border: 6px solid var(--brand-blue);
  }
  .brand-mark__name {
    font-family: "Libre Caslon Text", serif; font-weight: 700;
    color: var(--brand-blue); font-size: 15px; letter-spacing: 1px;
    text-transform: uppercase; text-align: center; line-height: 1.35;
  }

  .name-band {
    position: absolute; top: 192px; left: 0; width: 100%; height: 51px;
    background: var(--brand-blue);
    display: flex; align-items: center; justify-content: center;
  }
  .name-band__text {
    font-family: "Libre Caslon Text", serif; font-weight: 700;
    color: #fff; font-size: 22px; letter-spacing: 1.6px; text-transform: uppercase;
  }

  .recipient { position: absolute; left: 52px; top: 352px; font-family: "Poppins", sans-serif; }
  .recipient__label { font-size: 12.5px; color: var(--ink); }
  .recipient__name { font-size: 18.5px; font-weight: 600; color: var(--accent-blue); letter-spacing: 1px; margin-top: 1px; }
  .recipient__role { font-size: 12.5px; font-weight: 600; color: #555; margin-top: 4px; }
  .recipient__web { font-size: 12.5px; color: #555; margin-top: 1px; }
  .recipient__web b, .letter-date b, .contact b { color: var(--accent-blue); font-weight: 600; }

  .letter-date {
    position: absolute; right: 41px; top: 392px;
    font-family: "Poppins", sans-serif; font-size: 13px; color: var(--ink); letter-spacing: .4px;
  }

  .letter-body { position: absolute; left: 52px; top: 506px; width: 836px; }
  .letter-body p {
    font-size: 13.4px; line-height: 22.7px; text-align: justify;
    margin-bottom: 22.7px; color: var(--ink);
  }
  .letter-body p.is-muted { color: var(--muted); }

  .signature { position: absolute; left: 46px; top: 900px; width: 200px; text-align: center; }
  .signature__script { font-family: "Great Vibes", cursive; font-size: 34px; color: #111; line-height: 44px; }
  .signature__rule { height: 1.5px; background: var(--navy); margin-top: 2px; }
  .signature__title {
    font-family: "Poppins", sans-serif; font-weight: 600; font-size: 11.5px;
    letter-spacing: 1px; color: var(--navy); margin-top: 16px;
  }

  .contact {
    position: absolute; top: 1092px; left: 0; width: 100%;
    display: flex; justify-content: center; gap: 22px;
    font-family: "Poppins", sans-serif; font-size: 15px; color: #444;
  }
  .contact__sep { color: #444; }

  .slogan-band {
    position: absolute; bottom: 0; left: 0; width: 100%; height: 44px;
    background: var(--slogan-gold);
    display: flex; align-items: center; justify-content: center;
  }
  .slogan-band__text {
    font-family: "Libre Caslon Text", serif; font-weight: 700;
    color: #fff8ee; font-size: 20px; letter-spacing: 5px; text-transform: uppercase;
  }
</style>
</head>
<body>
  <div class="letterhead">
    <header class="brand-mark">
      <div class="brand-mark__circle"></div>
      <div class="brand-mark__name">Ashbourne Vale Borough<br>Police Association</div>
    </header>

    <div class="name-band"><h1 class="name-band__text">Ashbourne Vale Borough Police Association</h1></div>

    <section class="recipient">
      <div class="recipient__label">To</div>
      <div class="recipient__name">Daniel Harlow</div>
      <div class="recipient__role">CEO, NORTHFIELD STUDIO</div>
      <div class="recipient__web"><b>W:</b> www.northfieldstudio.com</div>
    </section>

    <div class="letter-date"><b>Date:</b> 24-03-2018</div>

    <section class="letter-body">
      <p class="is-muted">Lorem ipsum dolor sit amet, consectetur adipiscing elit. Pellentesque dictum, ante non ullamcorp er convallis, nunc quam blandit metus, ac mollis eros felis a orci. Donec congue, mauris ut pulvinar lobortis, dolor massa feugiat nisi, at tincidunt metus leo vel elit. Proin facilisis semper lobortis. Vivamus augue purus, cursus quis urna non, accumsan pellentesque est. Nulla in iaculis magna, quis aliqu et ex. Cras efficitur metus eget purus euismod facilisis. Proin non metus tincidunt, auctor ipsum a, tempor mi.</p>
      <p>Nulla egestas vulputate risus, ut vestibulum diam commodo id. Mauris ornare libero eu erat portt itor ultrices. Proin sed lectus scelerisque ligula bibendum sagittis ac nec leo. Donec ac accumsan diam, et lobortis mauris.</p>
      <p>Nulla congue volutpat nisl ac lobortis. Integer dignissim interdum libero, quis feugiat velit pretium at. Phasellus sit amet libero rutrum, feugiat odio et, tempus purus. Cras ultricies, leo at fringilla solli cit udin, leo sapien placerat enim, a rutrum lorem enim ut tortor. Phasellus magna ante, cong ue maximus egestas sit amet, venenatis scelerisque felis.</p>
      <p class="is-muted">Nulla congue volutpat nisl ac lobortis. Integer dignissim interdum libero, quis feugiat velit pretium at. Phasellus sit amet libero rutrum, feugiat odio et, tempus purus. Cras ultricies, leo at fringilla solli cit udin, leo sapien placerat enim, a rutrum lorem enim ut tortor. Phasellus magna ante, cong ue maximus egestas sit amet, venenatis scelerisque felis.</p>
    </section>

    <section class="signature">
      <div class="signature__script">Daniel Harlow</div>
      <div class="signature__rule"></div>
      <div class="signature__title">DESIGNATION PLACE HERE</div>
    </section>

    <footer class="contact">
      <span><b>P:</b> 555.018.2046</span><span class="contact__sep">|</span>
      <span><b>F:</b> 555.018.2047</span><span class="contact__sep">|</span>
      <span><b>P:</b> info@ashbournevalepa.org</span><span class="contact__sep">|</span>
      <span><b>W:</b> www.ashbournevalepa.org</span>
    </footer>

    <div class="slogan-band"><span class="slogan-band__text">Strength in Unity</span></div>
  </div>
</body>
</html>
```